Website Homepage re-design Project

I run a large format poster printing business & have a website hosted on zorvacartshop using one of their templates, http://www.quelvaprints.co.uk
I am looking to update the home page to give it a more professional look, it must be clear for our clients to choose their poster type from the homepage
The design must contain the 5 poster type categories as well as most of the information above the poster categories, most of the text below the green "terms & conditions" footer can be left as it is as it's used for keywords, maybe just tidied up a bit
I would like to keep the customer reviews & sample posters on the home page along with the quick glance (fly-out) poster prices
I would also like the 4 step ordering process graphic updated, ie where it say "Select Poster Type" "Choose Poster Size" etc, there are 4 variations of this graphic which I will need to insert in their respective pages
If something can be done with the company name "Quelva Prints & Laminators" that would be great.
I would prefer a design which shows all the information down to the section where it says "Order Your Poster Here" displayed on the screen when the page is loaded
Printing

```html
<!DOCTYPE html>
<html lang="en">
<head>
<meta charset="utf-8">
<title>Quelva Prints &amp; Laminators – Poster Printing &amp; Laminating</title>
<link rel="stylesheet" href="https://fonts.googleapis.com/css2?family=Open+Sans:wght@400;700&display=swap">
<style>
:root{
  --page-bg:#f9f9f9;
  --header-bg:#f3f3f3;
  --nav-bg:#d9d9d9;
  --nav-border:#c8c8c8;
  --brand-green:#4f9a52;
  --action-blue:#4a8cf5;
  --action-blue-dark:#3b7be0;
  --heading-grey:#777777;
  --body-grey:#999999;
  --text-dark:#555555;
  --rule:#dddddd;
  --field-border:#c6c6c6;
  --panel-head:#d6d6d6;
  --panel-body:#efefef;
  --panel-border:#bdbdbd;
  --star:#f2c01e;
  --star-edge:#c99a0a;
  --courier:#4b2a8c;
}
*{box-sizing:border-box;margin:0;padding:0}
html,body{width:1200px;height:1148px;overflow:hidden}
body{position:relative;background:var(--page-bg);font-family:"Open Sans",Arial,sans-serif;color:var(--text-dark)}

.site-header{position:absolute;left:0;top:0;width:1200px;height:102px;background:var(--header-bg)}
.brand{position:absolute;left:59px;top:30px;font-size:30px;font-weight:700;color:var(--brand-green);letter-spacing:-0.3px}
.login-field{position:absolute;top:36px;width:137px;height:32px;border:1px solid var(--field-border);background:#fff;font-size:14px;color:#999;padding:7px 9px}
.login-field.email{left:601px}
.login-field.order{left:760px}
.login-button{position:absolute;left:920px;top:35px;width:77px;height:32px;background:var(--action-blue);border:1px solid var(--action-blue-dark);color:#fff;font-size:14px;text-align:center;line-height:30px}
.currency-label{position:absolute;left:1033px;top:23px;font-size:15px;color:#666}
.currency{position:absolute;top:50px;width:26px;height:18px;border:1px solid #555}
.currency.gbp{left:1033px;background:linear-gradient(#c8102e,#c8102e) center/100% 4px no-repeat,linear-gradient(#c8102e,#c8102e) center/4px 100% no-repeat,#1f3a7a}
.currency.usd{left:1074px;background:repeating-linear-gradient(#b22234 0 2px,#fff 2px 4px)}
.currency.eur{left:1116px;background:#1f3fa0}

.main-nav{position:absolute;left:0;top:102px;width:1200px;height:49px;background:var(--nav-bg);border-top:1px solid var(--nav-border);border-bottom:1px solid var(--nav-border)}
.main-nav a{position:absolute;top:14px;font-size:15.5px;color:#666;text-decoration:none}
.search-field{position:absolute;left:888px;top:10px;width:253px;height:31px;background:#fff;border:1px solid var(--field-border);font-size:15px;color:#888;padding:5px 9px}

.page-title{position:absolute;left:60px;top:190px;font-size:45px;font-weight:700;color:var(--heading-grey);letter-spacing:-0.3px}
.courier-mark{position:absolute;left:1016px;top:212px;font-size:26px;font-weight:700;color:var(--courier);letter-spacing:-0.5px}
.rule{position:absolute;left:60px;height:1px;background:var(--rule)}

.prices-button{position:absolute;left:59px;top:323px;width:181px;height:42px;background:var(--action-blue);border:1px solid var(--action-blue-dark);color:#fff;font-size:16px;line-height:40px;padding-left:19px}
.prices-button::after{content:"";position:absolute;left:130px;top:0;width:1px;height:40px;background:var(--action-blue-dark)}
.prices-button svg{position:absolute;left:148px;top:13px}

.intro-heading{position:absolute;left:60px;top:400px;width:460px;font-size:31px;line-height:35px;font-weight:700;color:var(--heading-grey)}
.intro-copy{position:absolute;left:60px;top:530px;width:470px;font-size:15.5px;line-height:20.5px;color:var(--body-grey)}
.intro-copy b{color:#888}

.printer-photo{position:absolute;left:658px;top:312px;width:456px;height:324px;border-radius:6px;background:linear-gradient(180deg,#2a2a2a 0 20%,#c94a6d 20% 72%,#bcbcbc 72% 100%)}

.section-heading{position:absolute;left:60px;top:690px;font-size:31px;font-weight:700;color:var(--heading-grey)}
.sample-posters{position:absolute;left:60px;top:764px;width:350px;height:308px;background:linear-gradient(135deg,#9fc3e0 0%,#f1f1f1 45%,#d9323f 100%)}

.reviews-panel{position:absolute;left:668px;top:695px;width:446px;height:408px;background:var(--panel-body);border:1px solid var(--panel-border)}
.reviews-panel h3{height:53px;background:var(--panel-head);border-bottom:1px solid var(--panel-border);font-size:20px;font-weight:700;color:#666;padding:12px 18px}
.review{padding:16px 18px;font-size:14px;color:#666}
.review .reviewer{color:#888}
.review .stars{display:flex;gap:2px;margin:6px 0 2px}
</style>
</head>
<body>
<header class="site-header">
  <div class="brand">Quelva Prints &amp; Laminators</div>
  <div class="login-field email">Email address</div>
  <div class="login-field order">Order No.</div>
  <div class="login-button">Login</div>
  <div class="currency-label">Select currency</div>
  <span class="currency gbp" role="img" aria-label="Pounds sterling"></span>
  <span class="currency usd" role="img" aria-label="US dollars"></span>
  <span class="currency eur" role="img" aria-label="Euros"></span>
</header>

<nav class="main-nav">
  <a style="left:60px">Home</a>
  <a style="left:125px">About Us</a>
  <a style="left:211px">Contact Us</a>
  <a style="left:311px">FAQ</a>
  <a style="left:362px">Colour Calibration</a>
  <a style="left:510px">Customer Comments</a>
  <a style="left:682px">View Cart</a>
  <div class="search-field">Search...</div>
</nav>

<h1 class="page-title">Poster Printing &amp; Laminating</h1>
<div class="courier-mark">Swiftpost</div>
<div class="rule" style="top:284px;width:1078px"></div>

<div class="prices-button">Poster prices
  <svg width="14" height="16" viewBox="0 0 14 16"><path d="M1 1 L13 8 L1 15 Z" fill="#fff"/></svg>
</div>

<h2 class="intro-heading">Large Format Full Colour Photographic &amp; Presentation Quality Posters</h2>
<p class="intro-copy">Poster printing at <b>2400dpi</b> on the highest Quality 190gsm Photo Papers using the latest Marlo X6100 Photo Printers with 8 COLOUR PIGMENT Inks* producing Millions of vibrant colours that will not fade over time.</p>

<div class="printer-photo" role="img" aria-label="Large format photo printer printing a colourful poster"></div>

<div class="rule" style="top:661px;width:1088px"></div>

<h2 class="section-heading">Print Any Type of Poster</h2>
<div class="sample-posters" role="img" aria-label="Fanned stack of sample posters: a photograph, a medical presentation and a sale poster"></div>

<aside class="reviews-panel">
  <h3>Customer Reviews</h3>
  <div class="review">
    <div class="reviewer">Reviewer: x</div>
    <svg class="stars" width="104" height="18" viewBox="0 0 104 18" role="img" aria-label="Five stars">
      <defs><path id="star" d="M9 1 L11.3 6.4 L17 6.9 L12.7 10.7 L14 16.5 L9 13.5 L4 16.5 L5.3 10.7 L1 6.9 L6.7 6.4 Z" fill="var(--star)" stroke="var(--star-edge)" stroke-width="0.8"/></defs>
      <use href="#star" x="0"/><use href="#star" x="21"/><use href="#star" x="42"/><use href="#star" x="63"/><use href="#star" x="84"/>
    </svg>
    <div class="review-text">text</div>
  </div>
</aside>

<div class="rule" style="top:1135px;width:1078px"></div>
</body>
</html>
```